9x12 Business Brochure, 3 fold, for Internet Marketing Company

I'd like to have a brochure designed for my Internet marketing company. I have the content all ready, 10 Internet Marketing Myths, which you can see here: http://www.steadfernwebreach.com/common-internet-marketing-myths/. I'm looking for something creative and business to business. The company is all about Internet marketing. I like the "http://" header I use at our website. People like it too and identify with it. Audience is business owners 35 to 55 years old. I use blue at my website. I *think* I would like the cover page (front page) to open with some attention grabbing text, that basically takes most of the front page of the brochure. It would probably say: "I Can Help You Get BETTER RESULTS from Your Website, More Traffic, TOP RANKINGS at Zorvik, More Leads and MORE SALES. But first you'll have to avoid these common Internet marketing myths..." The inside pages would have the content from above (the 10 myths). The back page would have testimonials that I can provide. And the inside folded in page (or what I call the inside folded in page) would have a list of services. I think I want the dimensions 12x9 which is a larger sized, three-fold brochure.

Target Market(s)

I use this brochure to send to business owners and managers to show them I know what I'm talking about and and expert. See attachment for content.

Industry/Entity Type

Marketing

Requirements
Should not have
• No clipart. Probably not illustrations. Photos. The "http://" used at the site is something people "connect" with and get that this is about Internet marketing.

```html
<!DOCTYPE html>
<html lang="en">
<head>
<meta charset="utf-8">
<title>Services &amp; Expertise — Dana Merrow Consulting</title>
<link rel="stylesheet" href="https://fonts.googleapis.com/css2?family=Arimo&family=Indie+Flower&family=Poiret+One&family=Questrial&display=swap">
<style>
  :root {
    --paper: #ffffff;
    --navy: #0f4677;
    --blue: #1d5a8c;
    --blue-light: #2a6aa1;
    --ink: #333333;
    --footer: #111111;
  }
  * { margin: 0; padding: 0; box-sizing: border-box; }
  html, body { width: 1200px; height: 900px; overflow: hidden; background: var(--paper); }
  .spread { position: relative; width: 1200px; height: 900px; }

  .panel { position: absolute; top: 0; height: 900px; }
  .panel--services { left: 0; width: 400px; }
  .panel--cover { left: 800px; width: 400px; }

  .services__title {
    position: absolute; left: 40px; top: 30px;
    font-family: "Questrial", sans-serif; font-size: 35px; font-weight: 400;
    color: var(--navy); letter-spacing: -0.5px;
    text-shadow: 0 14px 6px rgba(15,70,119,0.12);
  }
  .services__list {
    position: absolute; left: 0; top: 86px; width: 404px;
    list-style: none; text-align: center;
    font-family: "Arimo", Arial, sans-serif; font-size: 17px; color: var(--blue);
  }
  .services__list li { height: 28.3px; line-height: 24px; }

  .handnote {
    position: absolute; text-align: center;
    font-family: "Indie Flower", cursive; font-size: 24px; line-height: 31px;
    color: var(--ink);
    text-shadow: 0 16px 5px rgba(0,0,0,0.12);
  }
  .handnote--quote { left: 20px; width: 360px; top: 656px; }
  .handnote--lead { left: 30px; width: 330px; top: 656px; }

  .pointer { position: absolute; left: 334px; top: 726px; width: 22px; height: 30px; }

  .contact {
    position: absolute; left: 0; top: 846px; width: 386px; text-align: center;
    font-family: "Arimo", Arial, sans-serif; font-size: 15px; line-height: 17px; color: var(--footer);
  }

  .headline {
    position: absolute; left: 22px; top: 32px;
    font-weight: 400; color: var(--blue-light);
  }
  .headline span { display: block; height: 57px; line-height: 57px; white-space: nowrap; }
  .headline .thin { font-family: "Poiret One", cursive; font-size: 44px; letter-spacing: -1.5px; font-weight: 700; }
  .headline .bold { font-family: "Questrial", sans-serif; font-size: 42px; color: var(--navy); letter-spacing: -0.5px; }
</style>
</head>
<body>
<main class="spread">
  <section class="panel panel--services">
    <h2 class="services__title">Services &amp; Expertise</h2>
    <ul class="services__list">
      <li>Internet Strategy Development</li>
      <li>Custom Website Design</li>
      <li>Blog Design &amp; Support</li>
      <li>Online Marketing Copywriting</li>
      <li>Social Media Marketing</li>
      <li>Search Engine Optimization (SEO)</li>
      <li>Conversion Optimization</li>
      <li>Content Marketing Management</li>
      <li>Using Frendly for Business</li>
      <li>Zorvik+, Vidora, Pinboardly</li>
      <li>Email Marketing &amp; Production</li>
      <li>Inquiry and Lead Development</li>
      <li>Zorvik AdSpot Pay-Per-Click</li>
      <li>Zorvik Local Places (maps)</li>
      <li>E-Commerce Development</li>
      <li>High-Performance Hosting</li>
      <li>Security &amp; Contingency Planning</li>
      <li>One-on-One or Group Training</li>
    </ul>
    <p class="handnote handnote--quote">"If you think its expensive to hire an expert, wait until you hire an amateur."</p>
    <p class="contact">Dana Merrow Consulting (.com)<br>(866) 555-0148</p>
  </section>

  <section class="panel panel--cover">
    <h1 class="headline">
      <span class="thin">I Can Help You Get</span>
      <span class="bold">BETTER</span>
      <span class="bold">RESULTS</span>
      <span class="thin">from Your webiste,</span>
      <span class="thin">More Traffic,</span>
      <span class="bold">TOP</span>
      <span class="bold">RANKINGS</span>
      <span class="thin">with Zorvik,</span>
      <span class="thin">More Inquiries, and</span>
      <span class="bold">MORE SALES</span>
    </h1>
    <p class="handnote handnote--lead">But first you'll need to avoid these Common Internet Marketing Myths...</p>
    <svg class="pointer" viewBox="0 0 22 30" aria-hidden="true">
      <path d="M2 2 L2 24 L7.5 19 L11.5 28 L15 26.5 L11 18 L18.5 18 Z" fill="#fff" stroke="#222" stroke-width="1.6" stroke-linejoin="round"/>
    </svg>
    <p class="contact">Dana Merrow Consulting (.com)<br>(866) 555-0148</p>
  </section>
</main>
</body>
</html>
```